Finance Company need Staff ID card & Patio umbrella design

We need the following design:
1. Employee ID Card (Vertical ID Card)
2. Patio Umbrella
3. Uniform (light grey collar shirt)

Please note that our company theme is grey and gold (yellow). Any mixture is fine as well as long it's simple, nice and unique.

Website: www.hlr-vantor.com.kh
Updates

Project Deadline Extended
Reason: Dear all We would like to extend deadline for 5 days more.

Target Market(s)

Public

Industry/Entity Type

Bank

Requirements
Must have
• 1. ID Card, information needed:
• - Name of the company: HLR Microfinance Ltd
• - Staff name
• - Position
• - ID #
• - Expiry Date
• - Photo
• - Message at the back of ID: This card is property of HLR Mirofinance Ltd. If found, Please return to HLR Microfinance Ltd 023 417 509.
• 2- Patio Umbrella only need company name
• 3- Uniform only need company and color design.
Nice to have
• Gold (or Yellow) and/or grey (Light)

```html
<!DOCTYPE html>
<html lang="en">
<head>
<meta charset="utf-8">
<title>HLR Microfinance – Staff ID Card (Back)</title>
<link href="https://fonts.googleapis.com/css2?family=Mulish:wght@400;600;700&display=swap" rel="stylesheet">
<style>
  :root {
    --bg: #5a5b5d;
    --navy: #253446;
    --gold: #d8b23a;
    --paper: #ffffff;
    --ink: #2b2f36;
    --muted: #4a4f57;
    --silver-light: #eceef0;
    --silver-dark: #9ea3a8;
  }
  * { box-sizing: border-box; margin: 0; padding: 0; }
  html, body {
    width: 1200px; height: 736px; overflow: hidden;
    background: var(--bg);
    font-family: "Mulish", sans-serif;
    color: var(--ink);
  }
  .canvas {
    width: 1200px; height: 736px;
    display: flex; align-items: center; justify-content: center;
  }
  .id-card {
    position: relative;
    width: 440px; height: 640px;
    background: var(--paper);
    display: flex; flex-direction: column;
  }
  .band { background: var(--navy); height: 44px; flex: none; }
  .band--top { border-bottom: 3px solid var(--gold); }
  .band--bottom {
    border-top: 3px solid var(--gold);
    height: 52px;
    display: flex; align-items: center; justify-content: center;
    color: #ffffff; font-size: 15px; letter-spacing: 0.04em;
  }
  .card-body { flex: 1; padding: 56px 40px 18px 40px; display: flex; flex-direction: column; }
  .info-row {
    display: grid; grid-template-columns: 140px 1fr;
    font-size: 14px; line-height: 1.45;
    margin-bottom: 44px;
  }
  .info-label { color: var(--muted); font-weight: 400; }
  .info-value { color: var(--ink); }
  .issuer {
    margin-top: auto;
    display: flex; align-items: center; justify-content: flex-end; gap: 14px;
    padding-right: 10px;
  }
  .issuer-label { font-size: 14px; font-weight: 700; color: var(--navy); }
  .issuer-seal { width: 64px; height: 64px; }
  .return-note {
    margin-top: 26px;
    font-size: 11px; line-height: 1.5; text-align: center; color: var(--muted);
  }
</style>
</head>
<body>
<main class="canvas">
  <article class="id-card">
    <div class="band band--top"></div>
    <section class="card-body">
      <div class="info-row">
        <span class="info-label">Office Address:</span>
        <span class="info-value">#41B, St. 207, Sangkat Boeung Raing, Khan Daun Penh, Phnom Penh, Cambodia</span>
      </div>
      <div class="info-row">
        <span class="info-label">Contact No:</span>
        <span class="info-value">(+855) 23 417 509<br>(+855) 90 31 6420</span>
      </div>
      <div class="info-row">
        <span class="info-label">Valid Till:</span>
        <span class="info-value">07/2019</span>
      </div>
      <div class="issuer">
        <span class="issuer-label">Issuing Authority</span>
        <svg class="issuer-seal" viewBox="0 0 64 64" aria-hidden="true">
          <defs>
            <radialGradient id="sealTone" cx="40%" cy="35%" r="70%">
              <stop offset="0%" stop-color="var(--silver-light)"/>
              <stop offset="100%" stop-color="var(--silver-dark)"/>
            </radialGradient>
          </defs>
          <circle cx="32" cy="32" r="30" fill="url(#sealTone)"/>
        </svg>
      </div>
      <p class="return-note">This card is property of HLR Mirofinance Ltd. If found,<br>Please return to HLR Microfinance Ltd 023 417 509.</p>
    </section>
    <footer class="band band--bottom">www.hlr-vantor.com.kh</footer>
  </article>
</main>
</body>
</html>
```